Kelvo Auto - help to get me noticed

We not long ago tasked Pixel Harbour to design a logo for my business. I'm happy with the result so would like to have a business card designed as a follow up.

It's an Automotive service and repair business that offers the following -
- Servicing
- General repairs
- Brakes
- Detailing
- Integrity

Kelvo Automotive
Dallin Mereth
0471 926 317

Target Market(s)

Everyday people with the ability to reach out to corporate customers also.

Industry/Entity Type

Automotive

Contact Information for Business Card

Black card, logo, name and phone number on front. Other details on back of card.

```html
<!DOCTYPE html>
<html lang="en">
<head>
<meta charset="utf-8">
<title>Kelvo Automotive – Business Card</title>
<link href="https://fonts.googleapis.com/css2?family=Montserrat:wght@700;800;900&family=Oswald:wght@600&display=swap" rel="stylesheet">
<style>
  :root {
    --backdrop: #3a3128;
    --card-black: #060606;
    --band-light: #a8d743;
    --band-dark: #4f9e36;
    --text-white: #f4f4f4;
    --text-dark: #111111;
    --brand-green: #8cc63f;
  }
  html, body {
    margin: 0;
    padding: 0;
    width: 900px;
    height: 1200px;
    overflow: hidden;
    background: var(--backdrop);
  }
  .canvas { display: block; width: 900px; height: 1200px; }
  .card-face { fill: var(--card-black); }
  .service-line {
    font-family: "Montserrat", sans-serif;
    font-weight: 800;
    fill: var(--text-white);
  }
  .service-line--accent { fill: url(#accentGradient); }
  .band-label {
    font-family: "Montserrat", sans-serif;
    font-weight: 800;
    fill: var(--text-dark);
  }
  .brand-name {
    font-family: "Montserrat", sans-serif;
    font-weight: 900;
    fill: var(--brand-green);
  }
  .phone-number {
    font-family: "Oswald", sans-serif;
    font-weight: 600;
    fill: var(--text-white);
  }
</style>
</head>
<body>
<svg class="canvas" viewBox="0 0 900 1200" xmlns="http://www.w3.org/2000/svg">
  <defs>
    <linearGradient id="bandGradient" x1="0" y1="0" x2="0" y2="1">
      <stop offset="0" stop-color="var(--band-light)"/>
      <stop offset="1" stop-color="var(--band-dark)"/>
    </linearGradient>
    <linearGradient id="accentGradient" x1="0" y1="0" x2="1" y2="0">
      <stop offset="0" stop-color="var(--band-dark)"/>
      <stop offset="1" stop-color="var(--band-light)"/>
    </linearGradient>
    <clipPath id="backCardClip"><rect x="75" y="133" width="768" height="437" rx="18"/></clipPath>
    <clipPath id="frontCardClip"><rect x="75" y="627" width="768" height="441" rx="18"/></clipPath>
  </defs>

  <!-- Services side -->
  <g class="card card--services" clip-path="url(#backCardClip)">
    <rect class="card-face" x="75" y="133" width="768" height="437"/>
    <rect class="side-band" x="733" y="133" width="110" height="437" fill="url(#bandGradient)"/>
    <text class="service-line" x="110" y="222" font-size="60" textLength="608" lengthAdjust="spacingAndGlyphs">GENERAL REPAIRS</text>
    <text class="service-line" x="108" y="341" font-size="152" textLength="610" lengthAdjust="spacingAndGlyphs">BRAKES</text>
    <text class="service-line service-line--accent" x="110" y="433" font-size="112" textLength="606" lengthAdjust="spacingAndGlyphs">INTEGRITY</text>
    <text class="service-line" x="110" y="530" font-size="118" textLength="590" lengthAdjust="spacingAndGlyphs">DETAILING</text>
    <text class="band-label" transform="translate(808 352) rotate(-90)" text-anchor="middle" font-size="48" textLength="345" lengthAdjust="spacingAndGlyphs">SERVICING</text>
  </g>

  <!-- Brand side -->
  <g class="card card--brand" clip-path="url(#frontCardClip)">
    <rect class="card-face" x="75" y="627" width="768" height="441"/>
    <rect class="side-band" x="75" y="627" width="108" height="441" fill="url(#bandGradient)"/>
    <text class="band-label" transform="translate(146 847) rotate(-90)" text-anchor="middle" font-size="40" textLength="350" lengthAdjust="spacingAndGlyphs">DALLIN MERETH</text>
    <text class="brand-name" text-anchor="middle">
      <tspan x="511" y="848" font-size="118" textLength="380" lengthAdjust="spacingAndGlyphs">KELVO</tspan>
      <tspan x="511" y="912" font-size="44" textLength="360" lengthAdjust="spacingAndGlyphs">AUTOMOTIVE</tspan>
    </text>
    <text class="phone-number" x="508" y="962" text-anchor="middle" font-size="40" textLength="238" lengthAdjust="spacingAndGlyphs">0471 926 317</text>
  </g>
</svg>
</body>
</html>
```